Create a proposal + product powerpoint

Please see the powerpoint for the slides. There are about 20 slides to be created. Rest of them are for reference and show the design that I like.

I would like to move fast on this, since I need to present it next week (in the week of April 21st).

Please download the current content from here:
https://www.filebrook-share.example/download/qTrVmXpLwZ8kDsYhNcBu

Please make at least 4 slides with the specific content so I can assess your design style.

Target Market(s)

Business Audience and very senior technical audience
Decision Makers

Industry/Entity Type

Product

Colors
e34297
a64599

Requirements
Must have
• Should be very clean, crisp.

I like to use Icons as shown in the powerpoint.... Please see the appendix of the slide deck that shows the various icons. Most of them just have plain text, and I would like to organize so that it does not look like some is just reading text.

I would like to focus on the design aspects so that the audience is clear on how the solution works.

Every page should some graphic element based on the slides shown in the appendix.

```html
<!DOCTYPE html>
<html lang="en">
<head>
<meta charset="utf-8">
<title>Project Plan</title>
<link rel="stylesheet" href="https://fonts.googleapis.com/css2?family=Roboto+Condensed:wght@400;700&display=swap">
<style>
  :root {
    --brand-purple: #a3178f;
    --title-purple: #a01b9a;
    --badge-purple: #8a4a8a;
    --milestone-purple: #8d4b8b;
    --milestone-label: #7b3a80;
    --header-pink: #f6d7ef;
    --footer-pink: #d6649c;
    --footer-light: #e8c4e1;
    --grid-line: #d9d9d9;
    --text-dark: #222222;
    --logo-grey: #8a8a8a;
    --white: #ffffff;
  }
  * { box-sizing: border-box; margin: 0; padding: 0; }
  html, body { width: 1200px; height: 900px; overflow: hidden; background: var(--white); }
  body { font-family: "Roboto Condensed", "Arial Narrow", sans-serif; color: var(--text-dark); }

  .slide { position: relative; width: 1200px; height: 900px; overflow: hidden; background: var(--white); }

  .slide-header {
    position: absolute; left: 0; top: 0; width: 1200px; height: 110px;
    background: linear-gradient(to bottom, var(--header-pink) 0%, #fbeef8 60%, var(--white) 100%);
  }
  .slide-title {
    position: absolute; left: 39px; top: 18px;
    font-size: 43px; font-weight: 400; color: var(--title-purple); letter-spacing: -0.5px;
  }
  .logo-placeholder {
    position: absolute; left: 1035px; top: 12px; width: 150px; height: 68px;
    background: var(--white); border: 2px solid #ecd7e7; border-radius: 9px;
    display: flex; align-items: center; justify-content: center;
    font-size: 28px; color: var(--logo-grey); letter-spacing: 1px;
  }

  .gantt { position: absolute; left: 82px; top: 108px; width: 1103px; }
  .gantt-row {
    position: relative; height: 43.5px; display: flex;
    border-top: 1px solid var(--grid-line);
  }
  .gantt-row:last-child { border-bottom: 1px solid var(--grid-line); }
  .task-label {
    width: 305px; padding-left: 10px; font-size: 17px; line-height: 43px;
    border-left: 1px solid var(--grid-line); border-right: 1px solid var(--grid-line);
  }
  .task-track { position: relative; flex: 1; border-right: 1px solid var(--grid-line); }
  .task-bar {
    position: absolute; top: 0; bottom: 0;
    background: var(--brand-purple);
    border-top: 2px solid #c052b0;
  }

  .phase-badge {
    position: absolute; left: 40.5px; width: 39px; height: 43.5px;
    background: var(--badge-purple); color: var(--white);
    font-size: 20px; font-weight: 700; display: flex; align-items: center; justify-content: center;
  }
  .phase-badge sup { font-size: 12px; margin-top: -8px; }

  .milestones-label {
    position: absolute; left: 84px; top: 762px;
    font-size: 30px; color: var(--milestone-label);
  }
  .milestone {
    position: absolute; top: 744px; height: 81px;
    background: var(--milestone-purple); border-radius: 4px; color: var(--white);
    text-align: center; line-height: 1.15; padding-top: 8px;
  }
  .milestone-name { font-size: 29px; font-weight: 700; }
  .milestone-name sup { font-size: 16px; }
  .milestone-time { font-size: 28px; }
  .milestone-time strong { font-weight: 700; }

  .slide-footer { position: absolute; left: 0; top: 859px; width: 1200px; height: 41px; }
  .footer-shapes { position: absolute; inset: 0; }
  .page-number { position: absolute; left: 12px; top: 9px; font-size: 19px; color: var(--white); }
  .copyright { position: absolute; right: 16px; top: 9px; font-size: 19px; color: var(--text-dark); }
</style>
</head>
<body>
<main class="slide">
  <header class="slide-header">
    <h1 class="slide-title">Project Plan</h1>
    <div class="logo-placeholder">LOGO HERE</div>
  </header>

  <section class="gantt" aria-label="Project schedule">
    <div class="gantt-row"><div class="task-label">Hire development team</div><div class="task-track"><span class="task-bar" style="left:3px;width:27px"></span></div></div>
    <div class="gantt-row"><div class="task-label">First phase - 6 weeks</div><div class="task-track"><span class="task-bar" style="left:30px;width:78px"></span></div></div>
    <div class="gantt-row"><div class="task-label">Security Review from Cloudmere</div><div class="task-track"><span class="task-bar" style="left:108px;width:159px"></span></div></div>
    <div class="gantt-row"><div class="task-label">Test - first Phase</div><div class="task-track"><span class="task-bar" style="left:108px;width:103.5px"></span></div></div>
    <div class="gantt-row"><div class="task-label">Test - Hosted first phase</div><div class="task-track"><span class="task-bar" style="left:211.5px;width:144px"></span></div></div>
    <div class="gantt-row"><div class="task-label">Build Second Phase</div><div class="task-track"><span class="task-bar" style="left:108px;width:103.5px"></span></div></div>
    <div class="gantt-row"><div class="task-label">Security Review - Second phase</div><div class="task-track"><span class="task-bar" style="left:211.5px;width:174px"></span></div></div>
    <div class="gantt-row"><div class="task-label">Test packaged version - second phase</div><div class="task-track"><span class="task-bar" style="left:211.5px;width:115.5px"></span></div></div>
    <div class="gantt-row"><div class="task-label">Test - Hosted third phase</div><div class="task-track"><span class="task-bar" style="left:387px;width:145.5px"></span></div></div>
    <div class="gantt-row"><div class="task-label">Build third phase</div><div class="task-track"><span class="task-bar" style="left:327px;width:147px"></span></div></div>
    <div class="gantt-row"><div class="task-label">Security Review - Second phase</div><div class="task-track"><span class="task-bar" style="left:474px;width:177px"></span></div></div>
    <div class="gantt-row"><div class="task-label">Test packaged version - second phase</div><div class="task-track"><span class="task-bar" style="left:474px;width:117px"></span></div></div>
    <div class="gantt-row"><div class="task-label">Test - Hosted third phase</div><div class="task-track"><span class="task-bar" style="left:651px;width:118.5px"></span></div></div>
    <div class="gantt-row"><div class="task-label">Ship to customer - Final Deliverable</div><div class="task-track"><span class="task-bar" style="left:769.5px;width:32px"></span></div></div>
  </section>

  <div class="phase-badge" style="top:152px">1<sup>st</sup></div>
  <div class="phase-badge" style="top:326px">2<sup>nd</sup></div>
  <div class="phase-badge" style="top:500px">3<sup>rd</sup></div>

  <p class="milestones-label">Milestones:</p>
  <div class="milestone" style="left:241.5px;width:228px">
    <div class="milestone-name">1<sup>st</sup> Phase</div>
    <div class="milestone-time">After <strong>3</strong> months</div>
  </div>
  <div class="milestone" style="left:508.5px;width:228px">
    <div class="milestone-name">2<sup>nd</sup> Phase</div>
    <div class="milestone-time">After <strong>5</strong> months</div>
  </div>
  <div class="milestone" style="left:786px;width:226.5px">
    <div class="milestone-name">3<sup>rd</sup> Phase</div>
    <div class="milestone-time">After <strong>7</strong> months</div>
  </div>

  <footer class="slide-footer">
    <svg class="footer-shapes" width="1200" height="41" viewBox="0 0 1200 41" aria-hidden="true">
      <polygon points="0,0 905,0 935,41 0,41" fill="var(--footer-pink)"/>
      <polygon points="920,0 1200,0 1200,41 950,41" fill="var(--footer-light)"/>
    </svg>
    <span class="page-number">Page : 01</span>
    <span class="copyright">Copyright text here</span>
  </footer>
</main>
</body>
</html>
```